We need a DL size flyer, double sided, for our lawn mowing and gardening business, Kestrel Yards.

We want to run on the front side, the following promotion:
50% off lawn mowing, applies to first lawn mowed on any regular service,
applies to first 100 callers only, so call now!
Professional lawn mowing at an affordable price.

Logo at the bottom left, with Lawn and Garden Maintenance written just below logo.

On bottom Right contact details;
Tom and Gareth
Ph: 0487650912
Email: kestrelyards@mailbox-demo.com
www.kestrelyards-demo.com.au

Front side positioned horizontally, with a bright and colour full design in the background, with the offer of 50% Off lawn mowing in large letters along the top.

On the rear side, also positioned horizontally, a list of our services, stating;

At Kestrel Yards we specialise in the following services;
Lawn mowing
Edging
Blowing
Hedging
Pruning
Tree Loping
Weeding
Poisoning
Mulching
Fertilising
Rubbish removal
Planting
Lawn care and advice
Turf
And any other garden maintenance job,
No job too big or too small.
(No particular order, whatever fits best)
Also include our contact details,
Kestrel Yards
Ph 0487650912
www.kestrelyards-demo.com.au

Target Market(s)

Home owners, aged between 30-50 years old, moderate socio ecenomic status to more afluent areas.

Industry/Entity Type

Business

Requirements
Must have
• DL size, front and back, full colour.
Nice to have
• The writting stating "Kestrel Yards" in our logo is quite bland, if that could also be amended to make it more appealing, but change the writting design only not the actual logo.

```html
<!DOCTYPE html>
<html lang="en">
<head>
<meta charset="utf-8">
<title>Kestrel Yards – DL Flyer</title>
<link href="https://fonts.googleapis.com/css2?family=Open+Sans:ital,wght@0,600;0,800;1,600&family=PT+Sans:wght@400;700&family=PT+Sans+Narrow:wght@400;700&display=swap" rel="stylesheet">
<style>
  :root {
    --headline-green: #0f6a2c;
    --brand-green: #1f7a2c;
    --band-light: #8fd324;
    --band-dark: #3b8a0c;
    --accent-yellow: #f5d000;
    --bullet-green: #5c9c14;
    --ink: #1a1a1a;
    --footer-ink: #0f2a10;
    --white: #ffffff;
    --divider: #2c5e10;
  }
  * { box-sizing: border-box; margin: 0; padding: 0; }
  html, body { width: 1182px; height: 1200px; overflow: hidden; background: #000; }
  .sheet { position: relative; width: 1182px; height: 1200px; background: #000; }

  .panel { position: absolute; left: 0; width: 1182px; height: 557px; overflow: hidden; }
  .panel--front { top: 0; }
  .panel--back { top: 643px; }

  .scene { position: absolute; left: 0; top: 0; width: 100%; height: 429px; }
  .scene--countryside {
    background: linear-gradient(180deg, #4fa6e4 0%, #a9d6f4 30%, #e6f3fb 52%, #a8d84a 66%, #7cc220 82%, #5aa414 100%);
  }
  .scene--garden {
    background: linear-gradient(180deg, #8fc6ee 0%, #dff0fb 40%, #f6fbfe 78%, #9ed43a 92%, #5fae14 100%);
  }

  .footer-band {
    position: absolute; left: 0; top: 429px; width: 100%; height: 128px;
    border-top: 8px solid var(--accent-yellow);
    background: radial-gradient(ellipse at 50% 20%, var(--band-light) 0%, #6cbb18 50%, var(--band-dark) 100%);
  }

  .headline {
    position: absolute; left: 0; width: 100%; top: 30px; text-align: center;
    font-family: "Open Sans", sans-serif; font-weight: 800; font-size: 80px; line-height: 1;
    color: var(--headline-green); letter-spacing: -1px;
    text-shadow: 0 0 2px #fff, 0 0 4px #dff7a8, 0 0 8px #9fe03a, 0 0 12px #6cc51a;
  }
  .offer-terms {
    position: absolute; left: 0; width: 100%; top: 134px; text-align: center;
    font-family: "PT Sans Narrow", sans-serif; font-size: 33px; line-height: 40px; color: var(--ink);
  }

  .brand-mark { position: absolute; left: 0; width: 100%; top: 296px; text-align: center; }
  .brand-mark__square { display: block; margin: 0 auto; width: 118px; height: 118px; background: var(--brand-green); }
  .brand-mark__name {
    display: block; margin-top: 32px;
    font-family: "PT Sans Narrow", sans-serif; font-weight: 700; font-size: 26px; line-height: 1;
    color: var(--footer-ink); letter-spacing: 0.5px;
  }

  .contact { position: absolute; left: 18px; top: 50px; width: 250px; text-align: center; color: var(--footer-ink); font-family: "PT Sans Narrow", sans-serif; }
  .contact__names { font-size: 16px; line-height: 18px; }
  .contact__phone { font-family: "PT Sans", sans-serif; font-weight: 700; font-size: 24px; line-height: 26px; }
  .contact__email { font-size: 14px; line-height: 18px; }

  .divider { position: absolute; top: 64px; width: 2px; height: 52px; background: var(--divider); }
  .divider--left { left: 354px; }
  .divider--right { left: 817px; }

  .service-line {
    position: absolute; left: 356px; width: 462px; top: 70px; text-align: center;
    font-family: "PT Sans Narrow", sans-serif; font-weight: 700; font-size: 35px; line-height: 40px; color: var(--footer-ink);
  }
  .web {
    position: absolute; left: 820px; width: 362px; top: 70px; text-align: center;
    font-family: "PT Sans Narrow", sans-serif; font-weight: 700; font-size: 24px; line-height: 28px; color: var(--footer-ink);
  }

  .services-intro {
    position: absolute; left: 64px; top: 56px;
    font-family: "PT Sans", sans-serif; font-size: 19px; line-height: 22px; color: var(--ink);
  }
  .services-list {
    position: absolute; left: 58px; top: 84px; width: 520px;
    list-style: none; display: grid; grid-template-columns: 304px 216px; grid-auto-flow: column; grid-template-rows: repeat(7, 30.4px);
    font-family: "PT Sans", sans-serif; font-weight: 700; font-size: 21px; line-height: 26px; color: var(--ink);
  }
  .services-list li { display: flex; align-items: center; }
  .services-list li::before {
    content: ""; width: 13px; height: 13px; margin: 0 14px 0 3px; background: var(--bullet-green); transform: rotate(45deg); flex: none;
  }
  .services-closing {
    position: absolute; left: 64px; top: 323px;
    font-family: "PT Sans", sans-serif; font-size: 18px; line-height: 25px; color: var(--ink);
  }

  .back-title {
    position: absolute; left: 640px; width: 512px; top: 56px; text-align: center;
    font-family: "PT Sans Narrow", sans-serif; font-weight: 700; font-size: 78px; line-height: 1;
    color: var(--white);
    text-shadow: 0 0 2px #2d8a12, 0 0 4px #3da318, 0 0 8px #7ed62a, 0 0 14px #b9ef5a;
  }
  .tagline {
    position: absolute; left: 640px; width: 512px; top: 150px; text-align: center;
    font-family: "Open Sans", sans-serif; font-style: italic; font-weight: 600; font-size: 20px; line-height: 26px; color: var(--ink);
  }
</style>
</head>
<body>
<div class="sheet">

  <section class="panel panel--front">
    <div class="scene scene--countryside" role="img" aria-label="Sunny countryside with rolling green hills, houses, a white picket fence and blossom branches"></div>
    <h1 class="headline">50% Off Lawn Mowing</h1>
    <p class="offer-terms">Applies to first lawn mowed on any<br>regular service and applies to first 100 callers only,<br>so call now!</p>

    <div class="footer-band">
      <div class="contact">
        <p class="contact__names">Tom and Gareth</p>
        <p class="contact__phone">Ph: 0487650912</p>
        <p class="contact__email">Email: kestrelyards@mailbox-demo.com</p>
      </div>
      <span class="divider divider--left"></span>
      <p class="service-line">Lawn &amp; Garden Maintenance</p>
      <span class="divider divider--right"></span>
      <p class="web">www.kestrelyards-demo.com.au</p>
    </div>

    <div class="brand-mark">
      <span class="brand-mark__square"></span>
      <span class="brand-mark__name">KESTREL YARDS</span>
    </div>
  </section>

  <section class="panel panel--back">
    <div class="scene scene--garden" role="img" aria-label="Bright sky over a grass edge with a yellow daisy and an orange butterfly"></div>

    <p class="services-intro">At Kestrel Yards we specialise in the following services;</p>
    <ul class="services-list">
      <li>Lawn mowing</li>
      <li>Blowing</li>
      <li>Pruning</li>
      <li>Weeding</li>
      <li>Mulching</li>
      <li>Rubbish removal</li>
      <li>Lawn care and advice</li>
      <li>Edging</li>
      <li>Hedging</li>
      <li>Tree Loping</li>
      <li>Poisoning</li>
      <li>Fertilising</li>
      <li>Planting</li>
      <li>Turf</li>
    </ul>
    <p class="services-closing">And any other garden maintenance job,<br>No job too big or too small.</p>

    <h2 class="back-title">Kestrel Yards</h2>
    <p class="tagline">Professional lawn mowing at an affordable price</p>

    <div class="footer-band">
      <div class="contact">
        <p class="contact__names">Tom and Gareth</p>
        <p class="contact__phone">Ph: 0487650912</p>
        <p class="contact__email">Email: kestrelyards@mailbox-demo.com</p>
      </div>
      <span class="divider divider--left"></span>
      <p class="service-line">Lawn &amp; Garden Maintenance</p>
      <span class="divider divider--right"></span>
      <p class="web">www.kestrelyards-demo.com.au</p>
    </div>

    <div class="brand-mark">
      <span class="brand-mark__square"></span>
      <span class="brand-mark__name">KESTREL YARDS</span>
    </div>
  </section>

</div>
</body>
</html>
```